Give my personal webpage more appeal!

I need my CV website improved - drmeganholt.com.au.
I am using the template KESTREL from pagecraftly. i would like to keep the already existing theme but am open to suggestions.
Please focus on imagery, colour scheme, and textures to enhance the appeal and look of the page.
The content is there, but now I need a designer to improve the look of my page.
I need styling, royalty-free unique modern images to make the page professional, personal and friendly.
I work in healthcare, so I'm a people person.
I teach professionals and I treat a lot of families.

Target Market(s)

Parents, Professional Healthcare providers

Number of Pages Required

1 page

Font styles to use
Serif
Sans Serif

Requirements
Must have
• My face - image at the top, all the information already contained in it.
• Links to the websites I manage such as my blog.
• One Page website.
• All the information it already contains with the ability to have more.
• Ideally, we would keep the same format for the page although I'm happy to expand column and change the page's structure with in the theme template KESTREL.
Nice to have
• The current KESTREL template. I would like to keep the already existing theme but am open to suggestions.
Should not have
• Multiple pages.

```html
<!DOCTYPE html>
<html lang="en">
<head>
<meta charset="utf-8">
<title>Dr Megan Holt – Chiropractor</title>
<link rel="stylesheet" href="https://fonts.googleapis.com/css2?family=Lato:wght@300;400;700&display=swap">
<style>
:root{
  --sidebar:#2a2a2a;
  --paper:#f9f9f9;
  --white:#ffffff;
  --ink:#1e1e1e;
  --body:#4a4a4a;
  --muted:#555555;
  --rule:#d8d8d8;
  --gold:#e8a128;
  --gold-btn:#d4951e;
  --footer:#252525;
  --field:rgba(120,120,120,.55);
  --field-text:#e4e4e4;
  --social:#7a7a7a;
}
*{margin:0;padding:0;box-sizing:border-box}
html,body{width:1146px;height:1200px;overflow:hidden}
body{position:relative;font-family:"Lato",sans-serif;background:var(--white);color:var(--ink)}
.sidebar{position:absolute;left:0;top:0;width:192px;height:1200px;background:var(--sidebar)}
.main{position:absolute;left:192px;top:0;width:954px;height:1200px}

.employment{position:absolute;left:0;top:0;width:954px;height:335px;background:var(--paper);border-bottom:1px solid #e2e2e2}
.section-title{position:absolute;left:0;width:100%;text-align:center;font-size:18px;font-weight:400;letter-spacing:.2px;color:var(--ink)}
.employment .section-title{top:56px}
.job{position:absolute;top:106px;width:176px}
.job-place{font-size:9.5px;text-transform:uppercase;color:var(--ink);line-height:15px}
.job-role{font-size:9.5px;text-transform:uppercase;color:var(--gold);line-height:15.5px}
.job-years{font-size:9.5px;color:var(--muted);line-height:16px;padding-bottom:3px;border-bottom:1px solid var(--rule)}
.job-role .job-years-inline{color:var(--muted);margin-left:14px}
.job-text{margin-top:15px;font-size:8.6px;font-weight:300;line-height:15.6px;color:var(--body);text-align:justify}

.sites{position:absolute;left:0;top:336px;width:954px;height:349px;background:var(--white)}
.sites .section-title{top:57px}
.site-tile{position:absolute;top:111px;width:180px;height:180px;border:1px solid #cfcfcf;display:flex;align-items:center;justify-content:center;font-size:17px;font-weight:700;text-decoration:none}
.site-tile--blog{left:59px;color:var(--gold);background:var(--white)}
.site-tile--gut{left:279px;background:#0b0f12;border-color:#0b0f12;color:#2f8fd0}
.site-tile--learn{left:499px;color:#1a1a1a;background:var(--white)}
.site-tile--reflex{left:717px;color:#111;background:var(--white)}

.contact{position:absolute;left:0;top:685px;width:954px;height:420px}
.contact-backdrop{position:absolute;inset:0;background:linear-gradient(90deg,#2c2a28 0%,#3a3530 35%,#4a4038 62%,#8a705c 80%,#5a4a3e 100%)}
.contact-shade{position:absolute;inset:0;background:rgba(20,20,20,.35)}
.contact .section-title{top:58px;color:var(--white);font-size:18px}
.contact-area{position:absolute;top:88px;width:100%;text-align:center;font-size:11.5px;font-weight:700;color:var(--gold)}
.contact-form{position:absolute;left:248px;top:130px;width:441px}
.field{display:block;width:441px;height:32px;margin-bottom:5px;background:var(--field);border:0;color:var(--field-text);font-family:"Lato",sans-serif;font-size:9.5px;text-align:center}
.field::placeholder{color:var(--field-text)}
.field--message{height:77px;padding-top:10px;resize:none}
.submit{position:absolute;left:168px;top:198px;width:105px;height:31px;background:var(--gold-btn);border:0;color:var(--white);font-family:"Lato",sans-serif;font-size:9.5px;font-weight:700}

.footer{position:absolute;left:0;top:1105px;width:954px;height:95px;background:var(--footer)}
.copyright{position:absolute;left:216px;top:44px;font-size:9.5px;color:#cfcfcf}
.footer-name{position:absolute;left:396px;top:36px;font-size:20px;font-weight:400;color:var(--gold)}
.social{position:absolute;top:38px;display:flex;align-items:center;gap:5px;font-size:9.5px;color:var(--social);text-decoration:none}
.social-dot{width:16px;height:16px;border-radius:50%;background:var(--social)}
.social--friendly{left:590px}
.social--linkwork{left:668px}
</style>
</head>
<body>
<div class="sidebar"></div>
<main class="main">

  <section class="employment">
    <h2 class="section-title">EMPLOYMENT</h2>

    <article class="job" style="left:59px">
      <p class="job-place">Little Spines Clinic</p>
      <p class="job-role">Founder, Chiropractor</p>
      <p class="job-years">2005-2017</p>
      <p class="job-text">What a wonderful place to work! I can't come to this clinic and not feel happy. It's decorated for the hundreds of children who get treated here. I've been privileged to watch so many families blossoms through the stages of infancy to teens. They feel like family.</p>
    </article>

    <article class="job" style="left:281px">
      <p class="job-place">Harbourside Spine &amp; Health Centre</p>
      <p class="job-role">Associate Chiropractor</p>
      <p class="job-years">2004-2005</p>
      <p class="job-text">I learned a lot from my mentor Dr Paul Hendry here. He taught me how to think like a business woman, which was exactly what I needed for my next move.</p>
    </article>

    <article class="job" style="left:502px">
      <p class="job-place">Clearwater Wellness Centre</p>
      <p class="job-role">Associate Chiropractor</p>
      <p class="job-years">2003-2004</p>
      <p class="job-text">Working under Dr Ross Talbot has been the greatest gift I could have imagined first year out of University. He taught me his life's learnings and I have treasured them. He taught me that the greatest gift for any teacher is to have their student surpass them.</p>
    </article>

    <article class="job" style="left:722px">
      <p class="job-place">Eastbrook University</p>
      <p class="job-role">Chiropractic Skills Tutor and<br>Examiner<span class="job-years-inline">2002</span></p>
      <p class="job-years" style="height:4px;line-height:4px;padding:0"></p>
      <p class="job-text">What an honour to be invited to tutor and examine 2nd year Chiropractic Skills whilst in my final year of my Masters of Chiropractic. And what a delightful bunch of students we had that year too!</p>
    </article>
  </section>

  <section class="sites">
    <h2 class="section-title">MY SITES</h2>
    <a class="site-tile site-tile--blog" href="#">Dr Megans blog</a>
    <a class="site-tile site-tile--gut" href="#">GutWise AU</a>
    <a class="site-tile site-tile--learn" href="#">kinesiolearn.com.au</a>
    <a class="site-tile site-tile--reflex" href="#">Reflex Roots</a>
  </section>

  <section class="contact">
    <div class="contact-backdrop" role="img" aria-label="Softly blurred photo of Dr Megan Holt smiling in her clinic with shelves behind her"></div>
    <div class="contact-shade"></div>
    <h2 class="section-title">CONTACT</h2>
    <p class="contact-area">WAVELL RISE Brisbane</p>
    <form class="contact-form">
      <input class="field" type="text" placeholder="Your Name">
      <input class="field" type="email" placeholder="Your Email">
      <input class="field" type="tel" placeholder="Your Phone Number">
      <textarea class="field field--message" placeholder="Your Message"></textarea>
      <button class="submit" type="button">Submit</button>
    </form>
  </section>

  <footer class="footer">
    <p class="copyright">© 2017 DR MEGAN HOLT</p>
    <p class="footer-name">Dr Megan Holt</p>
    <a class="social social--friendly" href="#"><span class="social-dot"></span>Friendly</a>
    <a class="social social--linkwork" href="#"><span class="social-dot"></span>Linkwork</a>
  </footer>

</main>
</body>
</html>
```